Price sign

Looking for a fresh new pricing sign.. with new prices size 2ft tall x 4ft wide , express lube $40.95, automatic transmission $129.95, radiator $109.95, Kestra Gold express lube $79.95, std trans/ diff $79.95, tuneup 4cyl $149.95, 6cyl $175.95 ,

```html
<!DOCTYPE html>
<html lang="en">
<head>
<meta charset="utf-8">
<title>Service Price Sign</title>
<link rel="stylesheet" href="https://fonts.googleapis.com/css2?family=Alfa+Slab+One&family=Bebas+Neue&family=Lobster&family=Oswald:wght@400;500;600&family=Ultra&display=swap">
<style>
  :root {
    --orange: #d86c3f;
    --navy: #2c4170;
    --red: #b03f3d;
    --white: #ffffff;
    --yellow: #f3e63a;
    --amber: #f7a93a;
    --brown: #5a2a14;
    --ink: #3a3a3a;
    --deep-navy: #1e2f57;
    --burst-red: #b8403a;
    --burst-orange: #e07a3e;
    --page: #ffffff;
  }
  * { margin: 0; padding: 0; box-sizing: border-box; }
  html, body { width: 1200px; height: 900px; overflow: hidden; background: var(--page); }
  .canvas { position: relative; width: 1200px; height: 900px; }
  .sign { position: absolute; left: 0; top: 148px; width: 1200px; height: 600px; display: grid; grid-template-columns: repeat(3, 400px); grid-template-rows: repeat(2, 300px); }
  .tile { position: relative; overflow: hidden; }
  .tile::after { content: ""; position: absolute; left: 15px; top: 14px; right: 15px; bottom: 14px; border: 3px solid var(--white); pointer-events: none; }
  .tile--orange { background: var(--orange); }
  .tile--navy { background: var(--navy); }
  .tile--red { background: var(--red); }
  .abs { position: absolute; white-space: nowrap; line-height: 1; }
  .decor { position: absolute; background: rgba(0,0,0,0.13); border-radius: 6px; }
  .smallcaps { font-family: "Oswald", sans-serif; font-variant: small-caps; font-weight: 500; color: var(--yellow); }
  .price { font-family: "Bebas Neue", "Oswald", sans-serif; color: var(--white); }
  .distressed { font-family: "Bebas Neue", "Oswald", sans-serif; color: var(--white); letter-spacing: 1px; }
  .burst { position: absolute; }

  /* Express lube */
  .lube-script { left: 50px; top: 22px; font-family: "Lobster", cursive; font-size: 40px; color: var(--brown); }
  .lube-title { left: 40px; top: 64px; font-family: "Ultra", serif; font-size: 66px; color: var(--white); text-shadow: 4px 4px 0 rgba(0,0,0,0.25); }
  .lube-sub { left: 44px; top: 136px; font-size: 21px; }
  .lube-can { left: 22px; top: 182px; width: 168px; height: 80px; }
  .lube-burst { left: 232px; top: 160px; width: 140px; height: 90px; }
  .lube-price { left: 250px; top: 187px; font-size: 38px; color: var(--ink); }

  /* Automatic transmission */
  .auto-block { left: 32px; top: 52px; transform: rotate(-5deg); transform-origin: left top; }
  .auto-time { font-family: "Oswald", sans-serif; font-variant: small-caps; font-size: 24px; color: var(--yellow); border-bottom: 3px solid var(--yellow); padding-bottom: 2px; display: inline-block; }
  .auto-title { font-family: "Alfa Slab One", serif; font-size: 32px; line-height: 1.05; color: var(--white); text-shadow: 3px 3px 0 var(--amber); margin-top: 6px; margin-left: 2px; }
  .auto-wrench { left: 190px; top: 150px; width: 150px; height: 135px; }
  .auto-price { left: 195px; top: 196px; font-size: 50px; text-shadow: 3px 3px 0 var(--amber); }

  /* Radiator */
  .rad-title { left: 34px; top: 32px; font-size: 70px; line-height: 0.95; }
  .rad-sub { left: 38px; top: 164px; font-family: "Oswald", sans-serif; font-size: 25px; color: var(--amber); }
  .rad-core { left: 215px; top: 172px; width: 175px; height: 118px; }
  .rad-price { left: 68px; top: 217px; font-size: 40px; }
  .rad-swoosh { position: absolute; left: 60px; top: 252px; }

  /* Kestra Gold express lube */
  .gold-brand { left: 42px; top: 40px; font-family: "Oswald", sans-serif; font-weight: 600; font-size: 18px; color: var(--white); }
  .gold-sub { left: 44px; top: 82px; font-size: 21px; }
  .gold-title { left: 38px; top: 108px; font-size: 74px; line-height: 0.95; }
  .gold-bottle { left: 300px; top: 80px; width: 95px; height: 220px; border-radius: 30px 30px 4px 4px; }
  .gold-dollar { left: 229px; top: 209px; width: 32px; height: 32px; border: 2px solid var(--yellow); border-radius: 50%; color: var(--yellow); font-family: "Oswald", sans-serif; font-size: 20px; display: flex; align-items: center; justify-content: center; }
  .gold-price { left: 266px; top: 203px; font-size: 46px; }
  .gold-swoosh { position: absolute; left: 232px; top: 246px; }

  /* Standard transmission / differential */
  .std-time { left: 38px; top: 40px; font-size: 24px; }
  .std-title { left: 42px; top: 72px; font-family: "Alfa Slab One", serif; font-size: 25px; line-height: 1.1; color: var(--white); }
  .std-or-line { position: absolute; left: 42px; width: 210px; top: 137px; height: 2px; background: var(--amber); }
  .std-or { left: 132px; top: 124px; font-family: "Lobster", cursive; font-size: 22px; color: var(--burst-red); background: var(--orange); padding: 0 4px; }
  .std-title-2 { top: 148px; }
  .std-burst { left: 230px; top: 178px; width: 140px; height: 100px; }
  .std-price { left: 252px; top: 209px; font-size: 40px; }

  /* Tune up */
  .tune-script { left: 128px; top: 26px; font-family: "Lobster", cursive; font-size: 42px; color: var(--deep-navy); }
  .tune-title { left: 0; width: 400px; text-align: center; top: 58px; font-size: 86px; font-weight: 400; }
  .tune-sub { left: 0; width: 400px; text-align: center; top: 138px; font-family: "Oswald", sans-serif; font-size: 25px; color: var(--yellow); }
  .tune-col { position: absolute; top: 186px; width: 114px; color: var(--white); }
  .tune-col--four { left: 30px; }
  .tune-col--six { left: 255px; }
  .tune-cyl { font-family: "Oswald", sans-serif; font-size: 20px; text-align: center; border-bottom: 3px solid var(--white); padding-bottom: 3px; line-height: 1; }
  .tune-price { font-family: "Bebas Neue", sans-serif; font-size: 44px; margin-top: 6px; line-height: 1; white-space: nowrap; }
</style>
</head>
<body>
<main class="canvas">
  <section class="sign">

    <article class="tile tile--orange">
      <div class="decor lube-can" role="img" aria-label="Faint oil can with drip"></div>
      <span class="abs lube-script">Express</span>
      <h2 class="abs lube-title">LUBE</h2>
      <p class="abs smallcaps lube-sub">14 Point Service</p>
      <svg class="burst lube-burst" viewBox="-1 -1 2 2" preserveAspectRatio="none"><polygon fill="var(--white)" points="1,0 .753,.202 .866,.5 .552,.552 .5,.866 .202,.753 0,1 -.202,.753 -.5,.866 -.552,.552 -.866,.5 -.753,.202 -1,0 -.753,-.202 -.866,-.5 -.552,-.552 -.5,-.866 -.202,-.753 0,-1 .202,-.753 .5,-.866 .552,-.552 .866,-.5 .753,-.202"/></svg>
      <span class="abs price lube-price">$ 40.95</span>
    </article>

    <article class="tile tile--navy">
      <div class="decor auto-wrench" role="img" aria-label="Faint crossed wrench and screwdriver"></div>
      <div class="abs auto-block">
        <span class="auto-time">30 Minute Service</span>
        <h2 class="auto-title">AUTOMATIC<br>TRANSMISSION</h2>
      </div>
      <span class="abs price auto-price">$129.95</span>
    </article>

    <article class="tile tile--red">
      <div class="decor rad-core" role="img" aria-label="Faint radiator core"></div>
      <h2 class="abs distressed rad-title">RADIATOR<br>SERVICE</h2>
      <p class="abs rad-sub">30 MINUTE SERVICE</p>
      <span class="abs price rad-price">$ 109.95</span>
      <svg class="rad-swoosh" width="124" height="14" viewBox="0 0 124 14"><path d="M2 11 Q60 2 122 4" stroke="var(--white)" stroke-width="3" fill="none" stroke-linecap="round"/></svg>
    </article>

    <article class="tile tile--red">
      <div class="decor gold-bottle" role="img" aria-label="Faint motor oil bottle"></div>
      <span class="abs gold-brand">Kestra Gold</span>
      <p class="abs smallcaps gold-sub">14 Point Service</p>
      <h2 class="abs distressed gold-title">EXPRESS<br>LUBE</h2>
      <span class="abs gold-dollar">$</span>
      <span class="abs price gold-price">79.95</span>
      <svg class="gold-swoosh" width="130" height="14" viewBox="0 0 130 14"><path d="M2 11 Q65 3 128 5" stroke="var(--yellow)" stroke-width="4" fill="none" stroke-linecap="round"/></svg>
    </article>

    <article class="tile tile--orange">
      <p class="abs smallcaps std-time">15 Minute Service</p>
      <h2 class="abs std-title">STANDARD<br>TRANSMISSION</h2>
      <div class="std-or-line"></div>
      <span class="abs std-or">Or</span>
      <h2 class="abs std-title std-title-2">DIFFERENTIAL<br>SERVICE</h2>
      <svg class="burst std-burst" viewBox="-1 -1 2 2" preserveAspectRatio="none">
        <polygon fill="var(--burst-red)" points="1,0 .753,.202 .866,.5 .552,.552 .5,.866 .202,.753 0,1 -.202,.753 -.5,.866 -.552,.552 -.866,.5 -.753,.202 -1,0 -.753,-.202 -.866,-.5 -.552,-.552 -.5,-.866 -.202,-.753 0,-1 .202,-.753 .5,-.866 .552,-.552 .866,-.5 .753,-.202"/>
        <polygon fill="var(--burst-orange)" transform="scale(.8)" points="1,0 .753,.202 .866,.5 .552,.552 .5,.866 .202,.753 0,1 -.202,.753 -.5,.866 -.552,.552 -.866,.5 -.753,.202 -1,0 -.753,-.202 -.866,-.5 -.552,-.552 -.5,-.866 -.202,-.753 0,-1 .202,-.753 .5,-.866 .552,-.552 .866,-.5 .753,-.202"/>
      </svg>
      <span class="abs price std-price">$ 79.95</span>
    </article>

    <article class="tile tile--navy">
      <span class="abs tune-script">Rocket's</span>
      <h2 class="abs distressed tune-title">TUNE UP</h2>
      <p class="abs tune-sub">60 MINUTE SERVICE</p>
      <div class="tune-col tune-col--four">
        <div class="tune-cyl">4 CYL</div>
        <div class="tune-price">$ 149.95</div>
      </div>
      <div class="tune-col tune-col--six">
        <div class="tune-cyl">6 CYL</div>
        <div class="tune-price">$175.95</div>
      </div>
    </article>

  </section>
</main>
</body>
</html>
```